Need label design for car cleaning spray bottle, big opportunity for repeat work

This is the first label design for a large assortment of car cleaning products. This design will be vital as it will set the design style for the remaining products. There is large opportunity for repeat work to the winning designer. For this first product we plan to call it "Interior Cleaner". We have the template label which we have attached to the project. The product is geared towards the market of Volmara car owners, and our logo also utilizes a similar font to what Volmara's company font uses.

We are looking to only update the design/format of the label. We will keep all text the same or modify it once the design is final. We will need to use our brand logo (attached).

We are looking for a minimalistic style design. Currently the label reads horizontally but we have noticed that the most successful brands that sell online have a vertical style design. We have attached some examples of brands such as "Gleam Bastion" and "Pivlo" which sell primarily on shopvendrix.com and have tens of thousands of reviews. We'd like to try and copy this label format as it seems very successful for these brands.

We are big fans of the minimal style that the brand "AutoZell" uses. Their label design emphasizes the name of the particular product in black text on a white background. The remainder of the label is color coded, and all of their products have a different color code while following the same diagonal design style. See attached examples.

So that being said, we would like to combine these 2 concepts, vertical alignment style with the minimalistic label design.

We are thinking of making the entire label white, and having an accent color like 1 large stripe that goes across the bottle, it would be an iconic part of the design as we will repeat this design across multiple products, similar to the AutoZell brand bundle example we attached. This specific product will be pink liquid (as you can tell the accent color is pink on the label).

We'd like to add a dynamic QR code (can use placeholder) on the label so customers can be directed to our website easily or any other page we choose in the future. We will also need a UPC barcode label (can use placeholder)

Target Market(s)

Volmara car owners

Industry/Entity Type

Car Detailing Products

Font styles to use
Sans Serif

Colors
E54698
E96AAD
F1A4CE
F9D9EA
FCEFF6

Requirements
Must have
• minimalistic design
Should not have
• no designs similar to brands like polish crew, dravonels, or any older brands in the category

```html
<!DOCTYPE html>
<html lang="en">
<head>
<meta charset="utf-8">
<title>Korveln All-Purpose Cleaner – Label Designs</title>
<link rel="stylesheet" href="https://fonts.googleapis.com/css2?family=Orbitron:wght@500&family=Exo+2:wght@300&family=Rajdhani:wght@700&family=Inter:wght@400;700&display=swap">
<style>
  :root {
    --pink: #E54698;
    --pink-soft: #E96AAD;
    --black: #0b0b0b;
    --white: #ffffff;
    --stage: #e6e7e7;
    --hazard: #ffe14a;
  }
  * { box-sizing: border-box; margin: 0; padding: 0; }
  html, body { width: 960px; height: 1200px; overflow: hidden; background: var(--stage); }
  .stage { position: relative; width: 960px; height: 1200px; }
  .label-slot { position: absolute; left: 204px; width: 552px; height: 528px; }
  .label-slot--white { top: 48px; }
  .label-slot--pink { top: 624px; }
  .label {
    position: absolute; left: 0; top: 0; width: 502px; height: 480px;
    transform: scale(1.1); transform-origin: 0 0;
    background: var(--white); overflow: hidden;
    font-family: "Inter", Arial, sans-serif; color: var(--black);
  }
  .label--pink { background: var(--pink); }

  .back-panel { position: absolute; left: 0; top: 0; width: 185px; height: 480px; background: var(--black); color: var(--white); }
  .label--pink .back-panel { width: 215px; }
  .accent-stripe { position: absolute; left: 185px; top: 0; width: 30px; height: 480px; background: var(--pink-soft); }
  .label--pink .accent-stripe { display: none; }

  .copy-block { position: absolute; left: 14px; width: 125px; }
  .copy-heading { font-weight: 700; font-size: 9px; color: var(--pink); margin-bottom: 2px; }
  .copy-body { font-size: 7px; line-height: 9px; }
  .copy-body p { margin-bottom: 4px; }
  .description { top: 20px; width: 120px; }
  .directions { top: 218px; width: 118px; }
  .directions .copy-body { font-size: 6.2px; line-height: 7.2px; }

  .maker { position: absolute; left: 16px; top: 367px; font-size: 6.4px; line-height: 8px; }
  .maker .site { color: var(--pink); font-weight: 700; font-size: 7px; margin-bottom: 8px; }
  .maker .company { font-weight: 700; font-size: 8.6px; line-height: 12px; }
  .maker .bold { font-weight: 700; }
  .maker .gap { height: 9px; }

  .vertical { position: absolute; transform: rotate(-90deg); transform-origin: 0 0; white-space: nowrap; }
  .product-type {
    left: 187px; top: 452px; width: 410px; height: 28px;
    font-family: "Exo 2", Arial, sans-serif; font-weight: 300; font-size: 26px; line-height: 28px;
    color: var(--white); letter-spacing: 0.5px;
  }
  .label--pink .product-type { color: var(--pink-soft); }
  .label--pink .product-type { filter: brightness(1.15); }
  .brand-name {
    left: 228px; top: 452px; width: 410px; height: 62px;
    font-family: "Orbitron", Arial, sans-serif; font-weight: 500; font-size: 54px; line-height: 62px;
    color: var(--black); letter-spacing: 2px;
  }
  .label--pink .brand-name { color: var(--white); }

  .claim-tag {
    height: 27px; background: var(--pink); color: var(--white);
    clip-path: polygon(7px 0, 100% 0, calc(100% - 7px) 100%, 0 100%);
    font-family: "Rajdhani", Arial, sans-serif; font-weight: 700; font-size: 10px; line-height: 10px;
    padding: 3px 0 0 10px; white-space: normal;
  }
  .label--pink .claim-tag { background: var(--black); }
  .claim-tag--formula { left: 300px; top: 428px; width: 82px; }
  .claim-tag--surfaces { left: 300px; top: 320px; width: 108px; }
  .claim-tag--grime { left: 300px; top: 190px; width: 136px; }

  .volume { position: absolute; left: 293px; top: 440px; width: 32px; text-align: center; font-size: 5.2px; line-height: 6px; }
  .label--pink .volume { color: var(--white); }

  .safety { position: absolute; left: 395px; top: 15px; width: 105px; font-size: 5.4px; line-height: 6.6px; }
  .safety-title { display: flex; align-items: center; gap: 3px; font-weight: 700; font-size: 8px; margin-bottom: 2px; }
  .safety-list { list-style: none; padding-left: 16px; }
  .safety-list li { text-indent: -3px; }
  .emergency { margin-top: 9px; padding-left: 16px; font-size: 4.8px; line-height: 6px; }

  .hazard-rating { position: absolute; left: 418px; top: 316px; display: flex; gap: 3px; }
  .hazard-table { border-collapse: collapse; font-size: 3.6px; font-weight: 700; }
  .hazard-table td { border: 0.5px solid var(--black); padding: 0 2px; height: 7px; }
  .hazard-table .key { width: 34px; color: var(--white); }
  .hazard-table .val { width: 7px; background: var(--white); text-align: center; }
  .row-health .key { background: #1f4fbf; }
  .row-flame .key { background: #d21e1e; }
  .row-react .key { background: #e8c400; color: var(--black); }
  .row-ppe .key { background: var(--white); color: var(--black); }
  .hazard-legend { font-size: 3.4px; line-height: 4.4px; font-weight: 700; }

  .harm-notice {
    position: absolute; left: 393px; top: 348px; width: 104px; height: 30px;
    background: var(--hazard); border: 2.5px dashed var(--black); border-radius: 4px;
    display: flex; align-items: center; gap: 5px; padding: 0 5px; font-size: 5.2px; line-height: 6px;
  }
  .harm-notice .harm-title { font-weight: 700; font-size: 7.6px; line-height: 8px; }
  .harm-notice .harm-text { text-align: center; flex: 1; }
  .harm-notice .harm-link { font-size: 4px; font-style: italic; }

  .net-content { position: absolute; left: 398px; top: 400px; width: 100px; text-align: center; font-weight: 700; font-size: 6px; line-height: 7px; }
  .code-slot { position: absolute; left: 400px; top: 418px; width: 88px; height: 39px; background: var(--white); border: 1px solid var(--black); }
  .label--pink .code-slot { background: var(--pink); border-color: var(--white); }
  .origin { position: absolute; left: 398px; top: 461px; width: 100px; text-align: center; font-style: italic; font-size: 5.6px; }
  .label--pink .net-content, .label--pink .origin { color: var(--white); }
</style>
</head>
<body>
<main class="stage">

  <div class="label-slot label-slot--white">
    <section class="label label--white" aria-label="Korveln all-purpose cleaner label, white version">
      <div class="back-panel">
        <div class="copy-block description">
          <h2 class="copy-heading">Description:</h2>
          <div class="copy-body">All-Purpose Cleaner is ready-to-use Hi-pH, non-corrosive, non-acidic, and non-caustic formula. It can be used on exterior surfaces such as wheel wells and engine bays and is also appropriate for the interior of your vehicle on surfaces such as door panels and dashboards.</div>
        </div>
        <div class="copy-block directions">
          <h2 class="copy-heading">Directions</h2>
          <div class="copy-body">
            <p>1. Spray the product directly on the surface to be cleaned and agitate with a towel.</p>
            <p>2. For heavy duty jobs, use carpet brush to agitate the surface.</p>
            <p>3. Immediately wipe the surface with clean towel or cloth and let it dry.</p>
          </div>
        </div>
        <div class="maker">
          <div class="site">www.website.com</div>
          <div>Manufactured for</div>
          <div class="company">Company Name</div>
          <div class="bold">Address</div>
          <div class="bold">City, State Zipcode</div>
          <div class="gap"></div>
          <div class="bold">P: Number</div>
          <div class="bold">E: Email</div>
          <div class="bold">www.website.com</div>
        </div>
      </div>
      <div class="accent-stripe"></div>
      <div class="vertical product-type">ALL-PURPOSE CLEANER</div>
      <div class="vertical brand-name">KORVELN</div>
      <div class="vertical claim-tag claim-tag--formula">NON ACIDIC<br>FORMULA</div>
      <div class="vertical claim-tag claim-tag--surfaces">INTERIOR<br>AND EXTERIOR</div>
      <div class="vertical claim-tag claim-tag--grime">REMOVES GREASE<br>GRIME AND DIRT</div>
      <div class="volume">16 FL. OZ.<br>(473 ML)</div>

      <div class="safety">
        <div class="safety-title">
          <svg width="13" height="13" viewBox="0 0 13 13" aria-hidden="true"><rect x="2.2" y="2.2" width="8.6" height="8.6" transform="rotate(45 6.5 6.5)" fill="#fff" stroke="#d21e1e" stroke-width="1.3"/><rect x="6" y="3.6" width="1" height="4" fill="#000"/><rect x="6" y="8.4" width="1" height="1" fill="#000"/></svg>
          WARNING:
        </div>
        <ul class="safety-list">
          <li>- Keep away from children.</li>
          <li>- May cause mild skin irritation.</li>
          <li>- Avoid eye contact.</li>
          <li>- If exposed, flush with water for 15 minutes and seek medical attention immediately</li>
        </ul>
        <div class="emergency">FOR EMERGENCY INFORMATION:<br>SAFELINE 800-555-0142</div>
      </div>

      <div class="hazard-rating">
        <table class="hazard-table">
          <tr class="row-health"><td class="key">HEALTH</td><td class="val">0</td></tr>
          <tr class="row-flame"><td class="key">FLAMMABILITY</td><td class="val">0</td></tr>
          <tr class="row-react"><td class="key">REACTIVITY</td><td class="val">0</td></tr>
          <tr class="row-ppe"><td class="key">PPE</td><td class="val">B</td></tr>
        </table>
        <div class="hazard-legend">KEY<br>4 - Severe<br>3 - Serious<br>2 - Moderate<br>1 - Slight<br>0 - Minimal</div>
      </div>

      <div class="harm-notice">
        <svg width="16" height="14" viewBox="0 0 16 14" aria-hidden="true"><path d="M8 1 L15 13 H1 Z" fill="#000"/><path d="M8 3.8 L12.8 12 H3.2 Z" fill="#ffe14a"/><rect x="7.4" y="6" width="1.2" height="3.4" fill="#000"/><rect x="7.4" y="10" width="1.2" height="1.2" fill="#000"/></svg>
        <div class="harm-text">
          <div class="harm-title">WARNING</div>
          <div>Cancer and<br>Reproductive Harm</div>
          <div class="harm-link">www.hazardnotes.info</div>
        </div>
      </div>

      <div class="net-content">NET 16 FL.OZ. (473 ML)<br>PART# KVAPC00716</div>
      <div class="code-slot" role="img" aria-label="Space reserved for QR code and UPC barcode"></div>
      <div class="origin">Made in America</div>
    </section>
  </div>

  <div class="label-slot label-slot--pink">
    <section class="label label--pink" aria-label="Korveln all-purpose cleaner label, pink version">
      <div class="back-panel">
        <div class="copy-block description">
          <h2 class="copy-heading">Description:</h2>
          <div class="copy-body">All-Purpose Cleaner is ready-to-use Hi-pH, non-corrosive, non-acidic, and non-caustic formula. It can be used on exterior surfaces such as wheel wells and engine bays and is also appropriate for the interior of your vehicle on surfaces such as door panels and dashboards.</div>
        </div>
        <div class="copy-block directions">
          <h2 class="copy-heading">Directions</h2>
          <div class="copy-body">
            <p>1. Spray the product directly on the surface to be cleaned and agitate with a towel.</p>
            <p>2. For heavy duty jobs, use carpet brush to agitate the surface.</p>
            <p>3. Immediately wipe the surface with clean towel or cloth and let it dry.</p>
          </div>
        </div>
        <div class="maker">
          <div class="site">www.website.com</div>
          <div>Manufactured for</div>
          <div class="company">Company Name</div>
          <div class="bold">Address</div>
          <div class="bold">City, State Zipcode</div>
          <div class="gap"></div>
          <div class="bold">P: Number</div>
          <div class="bold">E: Email</div>
          <div class="bold">www.website.com</div>
        </div>
      </div>
      <div class="accent-stripe"></div>
      <div class="vertical product-type">ALL-PURPOSE CLEANER</div>
      <div class="vertical brand-name">KORVELN</div>
      <div class="vertical claim-tag claim-tag--formula">NON ACIDIC<br>FORMULA</div>
      <div class="vertical claim-tag claim-tag--surfaces">INTERIOR<br>AND EXTERIOR</div>
      <div class="vertical claim-tag claim-tag--grime">REMOVES GREASE<br>GRIME AND DIRT</div>
      <div class="volume">16 FL. OZ.<br>(473 ML)</div>

      <div class="safety">
        <div class="safety-title">
          <svg width="13" height="13" viewBox="0 0 13 13" aria-hidden="true"><rect x="2.2" y="2.2" width="8.6" height="8.6" transform="rotate(45 6.5 6.5)" fill="#fff" stroke="#d21e1e" stroke-width="1.3"/><rect x="6" y="3.6" width="1" height="4" fill="#000"/><rect x="6" y="8.4" width="1" height="1" fill="#000"/></svg>
          WARNING:
        </div>
        <ul class="safety-list">
          <li>- Keep away from children.</li>
          <li>- May cause mild skin irritation.</li>
          <li>- Avoid eye contact.</li>
          <li>- If exposed, flush with water for 15 minutes and seek medical attention immediately</li>
        </ul>
        <div class="emergency">FOR EMERGENCY INFORMATION:<br>SAFELINE 800-555-0142</div>
      </div>

      <div class="hazard-rating">
        <table class="hazard-table">
          <tr class="row-health"><td class="key">HEALTH</td><td class="val">0</td></tr>
          <tr class="row-flame"><td class="key">FLAMMABILITY</td><td class="val">0</td></tr>
          <tr class="row-react"><td class="key">REACTIVITY</td><td class="val">0</td></tr>
          <tr class="row-ppe"><td class="key">PPE</td><td class="val">B</td></tr>
        </table>
        <div class="hazard-legend">KEY<br>4 - Severe<br>3 - Serious<br>2 - Moderate<br>1 - Slight<br>0 - Minimal</div>
      </div>

      <div class="harm-notice">
        <svg width="16" height="14" viewBox="0 0 16 14" aria-hidden="true"><path d="M8 1 L15 13 H1 Z" fill="#000"/><path d="M8 3.8 L12.8 12 H3.2 Z" fill="#ffe14a"/><rect x="7.4" y="6" width="1.2" height="3.4" fill="#000"/><rect x="7.4" y="10" width="1.2" height="1.2" fill="#000"/></svg>
        <div class="harm-text">
          <div class="harm-title">WARNING</div>
          <div>Cancer and<br>Reproductive Harm</div>
          <div class="harm-link">www.hazardnotes.info</div>
        </div>
      </div>

      <div class="net-content">NET 16 FL.OZ. (473 ML)<br>PART# KVAPC00716</div>
      <div class="code-slot" role="img" aria-label="Space reserved for QR code and UPC barcode"></div>
      <div class="origin">Made in America</div>
    </section>
  </div>

</main>
</body>
</html>
```